Barristers Chambers - Letterhead and Logo amendments

Marrowby Chambers is a barristers chambers in Thornbeck Rise, just around the corner from st. Orwins cathedral. We already have the logo and colour scheme but I think it can be improved, possibly with a better lettermark? we also have a small square version of it.
Main brand colour is: 671E75 – Purple.
Slogan: CONNECTING BARRISTERS, SOLICITORS AND OTHER PROFESSIONALS
I will attach both logos and also our current letterhead, which we made ourselves but it doesn't look professional enough.
Name of the Chambers: Marrowby Chambers
Tagline/Slogan (if any): None
Design Elements:
The logo should be simple and easy to recognize.
It should reflect the nature of the Chambers' work and be relevant to the legal industry.
Any images or graphics used should be unique, professional, and not overly complex.
The logo should be adaptable to various media, such as business cards, letterheads, and digital marketing materials.
It should be legible and easy to read, even when used at a small size.
The colour scheme should be professional and reflect the Chambers' brand identity.
Target Market(s)
Solicitors, lawyers and business clients
Industry/Entity Type
Legal

```html
<!DOCTYPE html>
<html lang="en">
<head>
<meta charset="utf-8">
<title>Marrowby Chambers – Letterhead</title>
<link rel="stylesheet" href="https://fonts.googleapis.com/css2?family=Arimo:wght@400;700&family=Mulish:wght@700&display=swap">
<style>
  :root {
    --brand-purple: #671e75;
    --backdrop: #cbc9ca;
    --paper: #ffffff;
    --ink: #555555;
    --ink-dark: #4a4a4a;
    --footer-grey: #666666;
    --signature-tone: #d9d9d9;
  }
  * { margin: 0; padding: 0; box-sizing: border-box; }
  html, body {
    width: 1173px; height: 1200px; overflow: hidden;
    background: var(--backdrop);
  }
  .letterhead {
    position: absolute; left: 230px; top: 96px;
    width: 713px; height: 1009px;
    background: var(--paper);
    font-family: "Arimo", Arial, sans-serif;
    color: var(--ink);
  }
  .brand {
    position: absolute; left: 0; right: 0; top: 54px; height: 60px;
    display: flex; justify-content: center; align-items: center;
  }
  .brand-row { display: flex; align-items: center; gap: 12px; }
  .brand-square {
    width: 56px; height: 56px;
    border: 2px solid var(--brand-purple);
  }
  .brand-name {
    font-family: "Arimo", Arial, sans-serif;
    font-weight: 400; font-size: 27px; letter-spacing: 0.5px;
    color: var(--brand-purple);
  }
  .salutation {
    position: absolute; left: 66px; top: 310px;
    font-family: "Mulish", sans-serif; font-weight: 700;
    font-size: 16px; color: var(--ink-dark);
  }
  .letter-body {
    position: absolute; left: 64px; top: 357px; width: 586px;
    font-size: 12px; line-height: 14.8px;
  }
  .letter-body p { margin-bottom: 12.4px; }
  .sign-off {
    position: absolute; left: 65px; top: 660px;
    font-family: "Mulish", sans-serif; font-weight: 700;
    font-size: 9px; color: var(--ink-dark);
  }
  .signature {
    position: absolute; left: 64px; top: 702px;
    width: 118px; height: 35px;
    background: var(--signature-tone); border-radius: 4px;
  }
  .footer-band {
    position: absolute; left: 0; top: 947px;
    width: 598px; height: 47px;
    background: var(--brand-purple); color: #fff;
    font-size: 11px;
  }
  .footer-address { position: absolute; left: 249px; top: 9px; white-space: nowrap; }
  .footer-contacts {
    position: absolute; right: 15px; top: 24px;
    display: flex; align-items: center; gap: 11px; white-space: nowrap;
  }
  .footer-contacts span { display: flex; align-items: center; gap: 9px; }
  .footer-contacts svg { width: 9px; height: 9px; fill: #fff; }
  .footer-mark {
    position: absolute; left: 603px; top: 947px;
    width: 47px; height: 47px;
    border: 2px solid var(--brand-purple); background: #fff;
  }
  .footer-block {
    position: absolute; left: 654px; top: 947px;
    width: 59px; height: 47px; background: var(--footer-grey);
  }
</style>
</head>
<body>
<main class="letterhead">
  <header class="brand">
    <div class="brand-row">
      <div class="brand-square"></div>
      <div class="brand-name">MARROWBY CHAMBERS</div>
    </div>
  </header>

  <div class="salutation">Dear Mr. Smith,</div>

  <section class="letter-body">
    <p>Lorem ipsum dolor sit amet, consectetuer adipiscing elit, sed diam nonmmy nibh euismod tincidunt ut laor eet dolore magna aliquam erat volutpat. Ut wisi enim ad minim veniam, quis nostrud exerci tationmcorper suscipit lobortis nisl ut aliquip ex ea commodo consequat. Duis autem vel eum iriure dolor in hendrerit in vulputate velit esse molestie consequat, vel illum dolore eu feugiat</p>
    <p>Rorem ipsum dolor sit amet, consectetuer adipiscing elit, sed diam nonmmy nibh euismod tincidunt ut laor eet dolore magna aliquam erat volutpat. Ut wisi enim ad minim veniam, quis nostrud exerci tationmcorper suscipit lobortis nisl ut aliquip ex ea commodo consequat. Duis autem vel eum iriure dolor in hendrerit in vulputate velit esse molest</p>
    <p>Dorem ipsum dolor sit amet, consectetuer adipiscing elit, sed diam nonmmy nibh euismod tincidunt ut laor eet dolore magna aliquam erat volutpat. Ut wisi enim ad minim veniam, quis nostrud exerci tationmcorper suscipit lobortis nisl ut aliquip ex ea commodo consequat. Duis autem vel eum iriure dolor in hendrerit in suscipit lobortis nisl ut aliquip ex ea commodo consequat. Duis autem vel eum iriure dolor in hendrerit in vulputate velit esse molestie consequat, vel illum</p>
    <p>Sorem ipsum dolor sit amet, consectetuer adipiscing elit, sed diam nonmmy nibh euismod tincidunt ut laor eet dolore magna aliquam erat volutpat. Ut wisi enim ad minim veniam, quis nostrud exerci tationmcorper suscipit lobortis nisl ut aliquip ex ea commodo consequat. Duis autem vel eum iriure dolor in</p>
  </section>

  <div class="sign-off">Sincerely,</div>
  <div class="signature" role="img" aria-label="Handwritten signature of the sender"></div>

  <footer>
    <div class="footer-band">
      <div class="footer-address">39 Thornbeck Rise, Suite 1, London EC4X 2QP</div>
      <div class="footer-contacts">
        <span>
          <svg viewBox="0 0 10 10" aria-hidden="true"><path d="M2 0.5 L3.6 2.6 L2.7 3.6 Q3.7 5.9 6.3 7.3 L7.4 6.4 L9.5 8 L8.4 9.5 Q4.5 9.3 1.6 5.9 Q0.3 3.6 0.6 1.5 Z"/></svg>
          01632 960481
        </span>
        <span>
          <svg viewBox="0 0 10 10" aria-hidden="true"><path d="M0.5 2 H9.5 V8 H0.5 Z M1 2.4 L5 5.4 L9 2.4" stroke="#671e75" stroke-width="0.7"/></svg>
          contact@marrowbychambers.co.uk
        </span>
        <span>
          <svg viewBox="0 0 10 10" aria-hidden="true"><circle cx="5" cy="5" r="4.5"/><path d="M0.5 5 H9.5 M5 0.5 V9.5" stroke="#671e75" stroke-width="0.7"/></svg>
          www.marrowbychambers.co.uk
        </span>
      </div>
    </div>
    <div class="footer-mark"></div>
    <div class="footer-block"></div>
  </footer>
</main>
</body>
</html>
```